Redesign B2B website

We are redesigning/ restructuring our current website. We provide company feedback surveys. We claim to be market leader in our country.
We like to be seen as a trustworthy, reliable and innovative partner to the top 1500 companies in the netherlands.
We want to be seen as a personal company.
Current website http://www.brivanto.nl does not meet our standards mentioned above.
Added Homepage layout. Please check
Target Market(s)
Large businesses, HR, decisiontakers
Industry/Entity Type
It Company
Requirements
Must have
- -The website is intended to be responsive. please take that into account. (propose plankor.es)
-The design should match our Style colors(will be provided)
- Wireframes are provided. Fonts used are Open Sans and Esteban,. Feel free to change things around.
Nice to have
- We like the design to be "flat", not much 3d effects, or icons.
Minimalist, Wordpress style or Metro style.

```html
<!DOCTYPE html>
<html lang="nl">
<head>
<meta charset="utf-8">
<title>Brivanto – Medewerkers- en klantenonderzoek</title>
<link rel="stylesheet" href="https://fonts.googleapis.com/css2?family=Open+Sans:ital,wght@0,300;0,400;0,600;1,300;1,400&display=swap">
<style>
:root{
  --navy:#0b2b66;
  --navy-deep:#0c2d58;
  --navy-bottom:#0a2750;
  --ink:#1b2a4a;
  --heading:#143a82;
  --link:#1d4f9a;
  --yellow:#f9b92e;
  --yellow-light:#fccf57;
  --hero-bg:#f0f0f3;
  --rule:#d9dce3;
  --foot-text:#c9d3e4;
}
*{margin:0;padding:0;box-sizing:border-box}
html,body{width:824px;height:1200px;overflow:hidden}
body{font-family:"Open Sans",Arial,sans-serif;color:var(--ink);background:#fff;position:relative}
.site-header{position:absolute;top:0;left:0;width:824px;height:101px;background:var(--navy);border-top:4px solid #15407f}
.brand{position:absolute;left:38px;top:32px;color:#fff}
.brand-name{font-size:22px;font-weight:600;line-height:26px}
.brand-tag{font-size:8.5px;font-weight:600;margin-top:2px}
.header-contact{position:absolute;right:24px;top:56px;display:flex;align-items:center;gap:14px;color:#fff;font-size:13px}
.social{display:flex;gap:7px}
.social span{width:17px;height:17px;border-radius:50%;background:#fff;display:block}
.main-nav{position:absolute;top:101px;left:0;width:824px;height:50px;background:linear-gradient(var(--yellow-light),var(--yellow));display:flex;align-items:center}
.main-nav a{color:var(--navy);text-decoration:none;font-size:12px;padding:0 16px;line-height:50px;border-right:1px solid rgba(0,0,0,.1)}
.main-nav a:first-child{padding-left:40px}
.main-nav a:nth-child(6){border-right:none}
.search-box{position:absolute;right:24px;top:14px;width:200px;height:23px;border-radius:12px;background:var(--yellow-light);font-size:9px;color:#6a5c30;padding:5px 13px}
.search-box svg{position:absolute;right:11px;top:5px}
.hero{position:absolute;top:151px;left:0;width:824px;height:294px;background:var(--hero-bg)}
.hero h1{position:absolute;left:36px;top:46px;width:340px;font-size:19.5px;font-weight:400;color:var(--heading);line-height:24px}
.hero p{position:absolute;left:36px;top:105px;width:340px;font-size:9px;line-height:17.7px;color:var(--link)}
.btn{position:absolute;left:34px;top:190px;width:85px;height:26px;border-radius:3px;background:#1e4f97;color:#fff;font-size:9px;text-align:center;line-height:26px}
.dots{position:absolute;left:41px;top:266px;display:flex;gap:4px}
.dots span{width:7px;height:7px;border-radius:50%;background:#9eb4d4}
.dots span:first-child{background:#1e4f97}
.hero-photo{position:absolute;left:404px;top:18px;width:389px;height:248px;background:#fff;padding:3px;box-shadow:0 0 3px rgba(0,0,0,.15)}
.hero-photo div{width:100%;height:100%;background:linear-gradient(135deg,#b88c6c,#e8d6c4 45%,#8aa2c0)}
.features{position:absolute;top:466px;left:20px;width:470px}
.feature{display:flex;gap:13px}
.feature .thumb{flex:none;width:86px;height:88px}
.feature h2{font-size:13px;font-weight:400;color:#111;margin:-2px 0 4px}
.feature p{font-size:8.8px;line-height:17.7px;color:#222}
.f1{position:absolute;top:0}.f2{position:absolute;top:117px}.f3{position:absolute;top:237px}
.aside{position:absolute;left:511px;top:466px;width:290px;height:315px;border-left:1px solid #eceef2}
.quote{position:absolute;left:18px;top:6px;width:265px;font-size:13.5px;font-style:italic;font-weight:300;line-height:17.7px;color:var(--heading)}
.partners{position:absolute;left:22px;top:154px;display:grid;grid-template-columns:repeat(4,56px);gap:18px 10px}
.partners span{height:40px;background:#d5d9e0;border-radius:4px}
.partners span:nth-child(2),.partners span:nth-child(8){border-radius:50%}
.contact-bar{position:absolute;top:831px;left:0;width:824px;height:51px;border-top:1px solid var(--rule);background:#fafafb}
.contact-bar .phone{position:absolute;left:28px;top:15px;display:flex;gap:12px;font-size:13.5px;color:var(--heading);align-items:center}
.contact-bar .social span{background:var(--heading)}
.newsletter{position:absolute;right:24px;top:11px;display:flex;align-items:center;font-size:9px;color:var(--link)}
.newsletter .field{width:158px;height:22px;background:#fff;border:1px solid #e2e4e8;margin-left:9px}
.newsletter .go{width:58px;height:22px;background:var(--yellow);color:var(--navy);line-height:22px;text-align:center;font-size:9.5px}
.site-footer{position:absolute;top:882px;left:0;width:824px;height:273px;background:var(--navy-deep);display:flex;padding-top:30px}
.col{border-right:1px solid #2a4b78;height:198px;padding-left:40px}
.col:last-child{border-right:none}
.col h3{font-size:13.5px;font-weight:400;color:#fff;margin-bottom:9px}
.col li{list-style:none;font-size:9.5px;color:var(--foot-text);line-height:19.3px}
.c1{width:185px}.c2{width:250px;padding-left:33px}.c3{width:193px;padding-left:33px}.c4{padding-left:32px}
.legal{position:absolute;top:1155px;left:0;width:824px;height:45px;background:var(--navy-bottom);border-top:1px solid #1d3c68;color:var(--foot-text);font-size:8.5px;text-align:center;line-height:45px}
</style>
</head>
<body>
<header class="site-header">
  <div class="brand">
    <div class="brand-name">Brivanto</div>
    <div class="brand-tag">Medewerkers- en klantenonderzoek</div>
  </div>
  <div class="header-contact">020-41 62 200- Contact
    <div class="social"><span></span><span></span><span></span><span></span><span></span></div>
  </div>
</header>
<nav class="main-nav">
  <a>Producten</a><a>Oplossingen</a><a>Branches</a><a>Kennis</a><a>Klanten</a><a>Over Brivanto</a>
  <div class="search-box">enter keyword
    <svg width="13" height="13" viewBox="0 0 13 13"><circle cx="5" cy="5" r="4" fill="none" stroke="#111" stroke-width="2"/><line x1="8" y1="8" x2="12" y2="12" stroke="#111" stroke-width="2.4"/></svg>
  </div>
</nav>
<section class="hero">
  <h1>Bevlogenheid en betrokkenheid stimuleren binnen uw organisatie?</h1>
  <p>Mauris neque metus, malesuada nec, ultricies sit amet, porttitor mattis, enim. In massa libero, interdum nec, interdum vel, blandit sed, nulla. In ullamcorper, est eget tempor cursus, neque mi consectetuer mi, a ultricies massa est sed nisl. Class aptent taciti sociosqu ad litora torquen.</p>
  <div class="btn">Learn More</div>
  <div class="dots"><span></span><span></span><span></span><span></span></div>
  <div class="hero-photo"><div role="img" aria-label="Groep lachende collega's"></div></div>
</section>
<section class="features">
  <article class="feature f1">
    <div class="thumb" role="img" aria-label="Vrouw in kantoor" style="background:linear-gradient(135deg,#8a6a58,#e9dfd6)"></div>
    <div><h2>Vivamus porttitor, neque at volutpat</h2>
    <p>Mauris neque metus, malesuada nec, ultricies sit amet, porttitor mattis, enim. In massa libero, interdum nec, interdum vel, blandit sed, nulla. In ullamcorper, est eget tempor cursus, neque mi consectetuer mi, a ultricies massa est sed nisl.</p></div>
  </article>
  <article class="feature f2">
    <div class="thumb" role="img" aria-label="Team van collega's" style="background:linear-gradient(135deg,#c9b3a2,#e07a8a 60%,#b5c6dc)"></div>
    <div><h2>Proin nulla arcu, nonummy luctus dictum eget</h2>
    <p>Mauris neque metus, malesuada nec, ultricies sit amet, porttitor mattis, enim. In massa libero, interdum nec, interdum vel, blandit sed, nulla. In ullamcorper, est eget tempor cursus, neque mi consectetuer mi, a ultricies massa est sed nisl. Class aptent taciti sociosqu ad litora torquent per conubia nostra</p></div>
  </article>
  <article class="feature f3">
    <div class="thumb" role="img" aria-label="Handen samen omhoog" style="background:linear-gradient(160deg,#7fb0d8,#d9c2b0 70%)"></div>
    <div><h2>Curabitur metus ipsum, luctus eu, malesuada ut.</h2>
    <p>Mauris neque metus, malesuada nec, ultricies sit amet, porttitor mattis, enim. In massa libero, interdum nec, interdum vel, blandit sed, nulla. In ullamcorper, est eget tempor cursus, neque mi consectetuer mi, a ultricies massa est sed nisl.</p></div>
  </article>
</section>
<aside class="aside">
  <blockquote class="quote">“Donec scelerisque leo ac risus. Praesent sit amet est. In dictum, dolor eu dictum porttitor, enim felis viverra mi, eget luctus massa purus quis odio. Etiam nulla massa, pharetra facilisis, volutpat in, imperdiet sit amet, sem. Aliquam nec erat at purus cursus interdum. ”</blockquote>
  <div class="partners"><span></span><span></span><span></span><span></span><span></span><span></span><span></span><span></span></div>
</aside>
<div class="contact-bar">
  <div class="phone">020-41 62 200 - Contact <div class="social"><span></span><span></span><span></span><span></span><span></span></div></div>
  <div class="newsletter">Praesent elementum elit at tellus<div class="field"></div><div class="go">Search</div></div>
</div>
<footer class="site-footer">
  <div class="col c1"><h3>Wat doen wij</h3><ul><li>Medewerkerstevredenheid</li><li>Veranderingsbereidheid</li><li>Verloopbestendigheid</li><li>Verzuimbestendigheid</li><li>Vitaliteit</li></ul></div>
  <div class="col c2"><h3>Waar kunnen we mee helpen</h3><ul><li>Waarom medewerkersonderzoek?</li><li>Werkwijze</li><li>Betrokkenheid</li><li>Effectiviteit</li><li>Efficiëntie</li><li>Klantgerichtheid</li><li>Leiderschap</li><li>Loyaliteit</li><li>Motivatie van medewerkers</li></ul></div>
  <div class="col c3"><h3>Ruime ervaring in</h3><ul><li>Waarom klantenonderzoek?</li><li>Werkwijze</li><li>B2B en B2C organisaties</li><li>CQ-index</li><li>Cliëntervaringsonderzoek</li><li>Patiëntenonderzoek</li><li>Klanttevredenheid</li><li>Klantloyaliteit</li><li>Imago</li></ul></div>
  <div class="col c4"><h3>Meer over ons</h3><ul><li>Vacatures en stages</li><li>Werken bij Brivanto</li><li>Open sollicitaties</li><li>Starters en professionals</li></ul></div>
</footer>
<div class="legal">© 2012 Brivanto. Medwerkers - en klanonderzoek &nbsp;|&nbsp; Privacy en Cookiebeleid &nbsp;|&nbsp; Algemene Voorwaarden</div>
</body>
</html>
```